Web Design Project - ReelHarbor Style Website

Hi there, we want to create a ReelHarbor / Flickden style website. We have a logo, and will be using a similar structure to this platform; http://tapecrate.example/v2/
Please feel free to be creative as possible, and make the site look however you would like :) keeping in mind the Ad space, and user friendly layout. We would like
1) The main page and
2) the video view page
designed
Updates
Logo and stock image uploaded
Hello; we most likely be basing the site on this tape crate theme, which also works as a mobile version.
Another option that I found for a layout which is different :)
http://www.quillnest-studio.example/demo-theme.cfm?theme=marvane
One last update; really like this one too
I am 100% likely to now use this format;
Target Market(s)
Bars, Cafe's, Restaurants, Attractions, Venues, Pubs, Wine and Dine
Industry/Entity Type
Reelharbor
Requirements
Must have
- Can be similar to ReelHarbor, but closer to Flickden's funky fresh look.
Should not have
- Not be too cluttered with too many videos on the home page. Feel free to think outside the box

```html
<!DOCTYPE html>
<html lang="en">
<head>
<meta charset="utf-8">
<title>Laneway Reels – Video View</title>
<link href="https://fonts.googleapis.com/css2?family=Arimo:wght@400;700&display=swap" rel="stylesheet">
<style>
:root{
  --header-dark:#4a4b4f;
  --header-light:#5b5c60;
  --header-rule:#b9babd;
  --text:#111;
  --white:#fff;
  --ad-green:#a9ba73;
  --panel-grey:#d5d5d5;
  --panel-border:#a7a7a7;
  --banner:rgba(58,58,62,.88);
  --progress:#5ab0e0;
}
*{box-sizing:border-box;margin:0;padding:0}
html,body{width:923px;height:1200px;overflow:hidden;background:var(--white)}
body{position:relative;font-family:"Arimo",Arial,sans-serif;color:var(--text)}
.site-header{position:absolute;left:0;top:0;width:923px;height:79px;
  background:linear-gradient(var(--header-light),var(--header-dark));
  border-bottom:9px solid var(--header-rule)}
.brand{position:absolute;left:67px;top:14px;color:var(--white);font-size:34px;font-weight:700;letter-spacing:-.5px}
.main-nav{position:absolute;right:69px;top:52px;display:flex;gap:15px}
.main-nav a{color:#e8e8e8;font-size:13px;font-weight:700;text-decoration:none}
.player{position:absolute;left:68px;top:98px;width:787px;height:443px;border:1px solid #333;
  background:radial-gradient(ellipse at 55% 55%,#8a3b2a 0%,#5a2a1a 45%,#2e1a12 100%)}
.now-watching{position:absolute;left:60px;top:113px;width:803px;height:35px;background:var(--banner);
  color:var(--white);font-size:22px;line-height:35px;padding-left:14px}
.now-watching b{margin-right:10px}
.controls{position:absolute;left:231px;top:482px;width:470px;height:35px;background:rgba(30,30,32,.75);border-radius:3px}
.video-copy{position:absolute;left:67px;top:574px;width:473px;font-size:14px;line-height:16.6px;text-align:justify}
.ad-space{position:absolute;left:604px;top:576px;width:199px;height:199px;background:var(--ad-green);border:1px solid #9aa969;
  color:var(--white);font-size:28px;line-height:23px;padding:27px 0 0 15px}
h2{position:absolute;font-weight:400;font-size:28px;left:67px}
.comments-title{top:792px}
.comment{position:absolute;top:836px;width:154px;font-size:12px;line-height:15.6px;text-align:justify}
.comment b{display:block}
.comment .more{font-weight:700}
.rating-panel{position:absolute;left:605px;top:822px;width:197px;height:168px;background:var(--panel-grey);border:2px solid var(--panel-border);
  padding:13px 0 0 13px;font-size:12px;line-height:15.5px}
.comment-box{width:168px;height:72px;background:var(--white);border:1px solid #aaa;border-radius:7px;margin-top:3px}
.videos-title{top:999px}
.thumb{position:absolute;top:1037px;width:153px;height:87px;border:1px solid #555}
.site-footer{position:absolute;right:72px;top:1155px;font-size:11px}
.site-footer b{font-weight:700}
</style>
</head>
<body>
<header class="site-header">
  <div class="brand">Laneway Reels</div>
  <nav class="main-nav"><a href="#">Search</a><a href="#">Featured Videos</a><a href="#">Recent Videos</a><a href="#">Top Channels</a><a href="#">Register</a><a href="#">Login</a></nav>
</header>

<div class="player" role="img" aria-label="Video still: hotel lounge with patterned daybeds, lamps and a fruit bowl on a low table"></div>
<div class="now-watching"><b>WATCHING:</b>The Marlowe Lodge</div>
<div class="controls">
  <svg width="470" height="35" viewBox="0 0 470 35">
    <rect x="20" y="11" width="3.5" height="13" fill="#fff"/><rect x="27" y="11" width="3.5" height="13" fill="#fff"/>
    <path d="M62 14h4l5-4v15l-5-4h-4z" fill="#fff"/><path d="M75 12v11M79 14v7" stroke="#fff" stroke-width="1.5"/>
    <rect x="95" y="14" width="268" height="7" rx="3.5" fill="#222"/>
    <rect x="95" y="14" width="115" height="7" rx="3.5" fill="#4e4e50"/>
    <rect x="95" y="14" width="88" height="7" rx="3.5" fill="var(--progress)"/>
    <text x="378" y="22" fill="#ccc" font-size="11" font-family="Arimo,sans-serif">1:57</text>
    <text x="427" y="23" fill="#ccc" font-size="13" font-weight="700" font-family="Arimo,sans-serif">HD</text>
    <path d="M456 9l7 0l0 7M463 9l-6 6M451 26l-7 0l0-7M444 26l6-6" stroke="#fff" stroke-width="2" fill="none"/>
  </svg>
</div>

<p class="video-copy">Lorem ipsum dolor sit amet, consectetur adipiscing elit. Mauris erat ipsum, gravida eget pellentesque at, blandit a purus. Aliquam scelerisque scelerisque massa, et eleifend orci ullamcorper vel. Morbi est erat, sodales id dapibus ac, consequat non ligula. Lorem ipsum dolor sit amet, consectetur adipiscing elit. Cum sociis natoque penatibus et magnis dis parturient montes, nascetur ridiculus mus. Mauris lacus dui, aliquam dapibus scelerisque quis, pharetra non orci. Morbi vitae diam nec libero pulvinar semper. Duis mi sapien, gravida a tincidunt eget, interdum vel justo. Nunc in risus ac sapien rutrum feugiat. Nulla eget magna neque. Curabitur egestas eros sapien, id ultricies sapien. Vivamus elementum fermentum erat eu varius. Fusce fermentum sollicitudin hendrerit. Sed enim mi, lacinia non vestibulum ac, interdum sed orci.</p>

<aside class="ad-space">advertisement space :)</aside>

<h2 class="comments-title">Recent Comments:</h2>
<div class="comment" style="left:68px"><b>By: sam.ortega85</b>This hotel looks awesome! The staff looks friendly, the rooms look awesome, and the best thing is that it's got a pool! I'm planning to stay there during my vacation. What do you guys think? Are there any better...<br><span class="more">(Read More)</span></div>
<div class="comment" style="left:235px"><b>By: sam.ortega85</b>This hotel looks awesome! The staff looks friendly, the rooms look awesome, and the best thing is that it's got a pool! I'm planning to stay there during my vacation. What do you guys think? Are there any better...<br><span class="more">(Read More)</span></div>
<div class="comment" style="left:400px"><b>By: sam.ortega85</b>This hotel looks awesome! The staff looks friendly, the rooms look awesome, and the best thing is that it's got a pool! I'm planning to stay there during my vacation. What do you guys think? Are there any better...<br><span class="more">(Read More)</span></div>

<section class="rating-panel">
  <div>Video Rating: <b>4.3 /5</b></div>
  <div>Rate this video:</div>
  <svg width="100" height="16" viewBox="0 0 100 16">
    <g fill="#e3c24a" stroke="#9a8030" stroke-width=".6">
      <path id="star" d="M8 1l2 5h5l-4 3 1.6 5L8 11 3.4 14 5 9 1 6h5z"/>
      <use href="#star" x="20"/><use href="#star" x="40"/><use href="#star" x="60"/>
    </g>
    <use href="#star" x="80" fill="#eee" stroke="#888" stroke-width=".6"/>
  </svg>
  <div>Leave a Comment:</div>
  <div class="comment-box"></div>
</section>

<h2 class="videos-title">Most recent videos:</h2>
<div class="thumb" style="left:68px;background:linear-gradient(135deg,#e8dcae,#b9a97a)" role="img" aria-label="Video thumbnail: bright retail shop interior"></div>
<div class="thumb" style="left:226px;background:linear-gradient(#8a6a4a,#4c7a86)" role="img" aria-label="Video thumbnail: hotel pool at dusk"></div>
<div class="thumb" style="left:384px;background:linear-gradient(135deg,#6a4a30,#2a1c14)" role="img" aria-label="Video thumbnail: hotel bedroom"></div>
<div class="thumb" style="left:542px;background:linear-gradient(#7a5a40,#3a2a20)" role="img" aria-label="Video thumbnail: grand lobby staircase"></div>
<div class="thumb" style="left:700px;background:linear-gradient(#c9ccd0,#9a3a3a)" role="img" aria-label="Video thumbnail: shuttle bus at a stop"></div>
<svg width="923" height="1200" style="position:absolute;left:0;top:0;pointer-events:none" aria-hidden="true">
  <g fill="#fff" opacity=".9">
    <path d="M140 1073l10 7-10 7z"/><path d="M298 1073l10 7-10 7z"/><path d="M456 1073l10 7-10 7z"/><path d="M614 1073l10 7-10 7z"/><path d="M772 1073l10 7-10 7z"/>
  </g>
</svg>

<footer class="site-footer">Copyright © 2012 - 2013 &nbsp;<b>lanewayreels.example</b></footer>
</body>
</html>
```